Texas Recycling and dump company needs Flyer design

We need a flyer design for a new company based in Austin Texas called 'Salvage Grove'. We receive dump materials on our property along with sell repurposed materials. We would like our design to include our logo along with add some creative designs to the flyer. Please use the attached image file as an outline. Blank boxes can be used for additional images.

Target Market(s)

Handing out flyers to new companies and hopefully getting contracts with them.

Font styles to use
Serif
Sans Serif

Requirements
Must have
• double sided
• images
Nice to have
• QR code with our website

```html
<!DOCTYPE html>
<html lang="en">
<head>
<meta charset="utf-8">
<title>Salvage Grove Flyer</title>
<link rel="stylesheet" href="https://fonts.googleapis.com/css2?family=Montserrat:wght@400;500;600;700&family=PT+Serif:wght@400&family=Oswald:wght@400;500&display=swap">
<style>
  :root{
    --bg:#e9ecef;
    --paper:#ffffff;
    --panel:#f4f4f4;
    --green:#7cc04f;
    --green-dark:#5ea83a;
    --blue:#1565b5;
    --ink:#1d1d1d;
    --grey-text:#555;
    --rule:#e8d48a;
  }
  *{margin:0;padding:0;box-sizing:border-box}
  html,body{width:1200px;height:1200px;overflow:hidden;background:var(--bg)}
  .flyer{position:absolute;left:209px;top:46px;width:782px;height:1107px;background:var(--paper);box-shadow:0 4px 14px rgba(0,0,0,.18);overflow:hidden;font-family:'Montserrat',sans-serif;color:var(--ink)}
  .abs{position:absolute}
  .brand{left:40px;top:70px;display:flex;align-items:center;gap:10px;font-weight:700;font-size:24px;color:var(--blue);letter-spacing:.5px}
  .brand-dot{width:18px;height:18px;border-radius:50%;background:var(--green)}
  .tagline{left:296px;top:53px;width:486px;height:30px;background:#f0f0f0;font-size:14px;letter-spacing:3.4px;color:#444;line-height:30px;padding-left:25px}
  .tagline b{font-weight:700}
  .tagline-end{right:0;top:53px;width:40px;height:30px;background:var(--blue)}
  .top-url{left:320px;top:93px;font-size:11px;font-weight:500}
  .hero-photo{left:0;top:138px;width:391px;height:309px;background:radial-gradient(circle at 45% 45%,#6fae3a 0,#3f7a25 35%,#9ccc5a 70%,#4e8a2e 100%)}
  .hero-panel{left:391px;top:138px;width:391px;height:309px;background:linear-gradient(135deg,var(--green-dark),var(--green) 60%,#8fcb5f)}
  .motto{left:51px;font-family:'PT Serif',serif;font-size:58px;color:#fff;line-height:1}
  .motto-rule{left:51px;top:245px;width:294px;height:1px;background:#fff}
  .motto-sub{left:51px;top:263px;font-family:'Oswald',sans-serif;font-size:21px;letter-spacing:1.5px;color:#fff}
  .lower-panel{left:391px;top:447px;width:391px;height:660px;background:var(--panel)}
  .rule{left:47px;width:688px;height:1px;background:var(--rule)}
  .overview{left:47px;top:482px;font-size:15px;font-weight:700;letter-spacing:1.5px}
  .tile{width:210px;height:115px}
  .label{width:210px;text-align:center;font-size:15px;font-weight:700;letter-spacing:1.2px}
  .slogan{left:0;width:734px;top:904px;text-align:center;font-family:'Oswald',sans-serif;font-size:31px;letter-spacing:2px;color:var(--blue)}
  .phone-bar{left:80px;top:964px;width:311px;height:86px;background:var(--green)}
  .phone-icon{left:47px;top:964px}
  .phone-number{left:150px;top:972px;font-family:'Oswald',sans-serif;font-size:40px;letter-spacing:3px;color:#fff;line-height:70px}
  .pin{left:416px;top:972px}
  .address{left:487px;top:970px;font-size:18px;line-height:24px;color:var(--grey-text);font-weight:500}
  .address strong{font-weight:700}
  .bottom-url{left:0;width:782px;top:1072px;text-align:center;font-size:17px;font-weight:600;letter-spacing:1.5px}
</style>
</head>
<body>
<main class="flyer">
  <div class="abs brand"><span class="brand-dot"></span>SALVAGE GROVE</div>
  <div class="abs tagline">GIVE YOUR GARBAGE <b>ANOTHER LIFE</b></div>
  <div class="abs tagline-end"></div>
  <div class="abs top-url">www.salvagegrove.com</div>

  <div class="abs hero-photo" role="img" aria-label="Hand holding a green globe topped with fresh leaves against a blurred forest"></div>
  <section class="abs hero-panel">
    <div class="abs motto" style="top:35px">REDUCE</div>
    <div class="abs motto" style="top:107px">REUSE</div>
    <div class="abs motto" style="top:179px">RECYCLE</div>
    <div class="abs motto-rule"></div>
    <div class="abs motto-sub">FOR A BETTER TOMORROW</div>
  </section>

  <div class="abs lower-panel"></div>
  <div class="abs rule" style="top:468px"></div>
  <div class="abs overview">OVERVIEW</div>

  <div class="abs tile" style="left:47px;top:530px;background:linear-gradient(135deg,#4a4d52,#8d9096 55%,#3f4247)" role="img" aria-label="Pile of concrete blocks"></div>
  <div class="abs tile" style="left:286px;top:530px;background:linear-gradient(135deg,#3a3b3e,#505256 50%,#3c3d40)" role="img" aria-label="Close-up of asphalt surface"></div>
  <div class="abs tile" style="left:524px;top:530px;background:linear-gradient(180deg,#d9c9a6 0,#a88a5e 35%,#8e7048 100%)" role="img" aria-label="Mound of clean fill dirt"></div>
  <div class="abs label" style="left:47px;top:660px">CONCRETE</div>
  <div class="abs label" style="left:286px;top:660px">ASPHALT</div>
  <div class="abs label" style="left:524px;top:660px">CLEAN FILL</div>

  <div class="abs tile" style="left:167px;top:730px;background:linear-gradient(135deg,#c9955a,#e7c48e 50%,#a46f38)" role="img" aria-label="Heap of broken wood and brush"></div>
  <div class="abs tile" style="left:406px;top:730px;background:linear-gradient(180deg,#9a8a78 0,#7c5a40 45%,#c9c3b8 100%)" role="img" aria-label="Construction and demolition debris pile in a yard"></div>
  <div class="abs label" style="left:167px;top:860px">WOOD/ BRUSH</div>
  <div class="abs label" style="left:406px;top:860px">C&amp;D</div>

  <div class="abs slogan">CLEANER THE PRODUCT, LOWER THE PRICE</div>

  <div class="abs phone-bar"></div>
  <svg class="abs phone-icon" width="88" height="88" viewBox="0 0 88 88" aria-hidden="true">
    <circle cx="43" cy="43" r="43" fill="#1565b5"/>
    <circle cx="43" cy="43" r="36" fill="#fff"/>
    <circle cx="43" cy="43" r="32" fill="#9c9c9c"/>
    <path d="M30 27c3-2 5-1 6 1l4 7c1 2 0 4-2 5l-2 1c2 5 6 9 11 11l1-2c1-2 3-3 5-2l7 4c2 1 3 3 1 6l-3 3c-3 2-9 1-16-4-7-5-12-12-14-18-1-5 0-9 3-12z" fill="#111"/>
  </svg>
  <div class="abs phone-number">512 555 0148</div>

  <svg class="abs pin" width="50" height="70" viewBox="0 0 50 70" aria-hidden="true">
    <path d="M25 0C11 0 0 11 0 25c0 18 25 45 25 45s25-27 25-45C50 11 39 0 25 0z" fill="#111"/>
    <circle cx="25" cy="24" r="10" fill="#fff"/>
  </svg>
  <div class="abs address"><strong>SALVAGE GROVE</strong><br>2180, CEDAR HOLLOW RD<br>AUSTIN, TEXAS</div>

  <div class="abs rule" style="top:1064px"></div>
  <div class="abs bottom-url">www.salvagegrove.com</div>
</main>
</body>
</html>
```